One Page / Executive Summary for Silverpine Executive Search

We would need an executive summary for our firm Silverpine Executive Search - like a small one pager which we can via PDF to our clients.
It should include like the file 23030 all Infos - Only Track Record needs to be complemented
But it should be designed much nicer than it is now - also open for new design situations but it should fit our website concept www.silverpinexs.io
It should also include a graph of the recruiting process - maybe draw a new one.?
We would need a very elegant, modern, slim design, it should look very female - it should not have a green color block on the top but be more sleek bright and with our bird
Target Market(s)
CEO, HR executives
Industry/Entity Type
HR Consultantcy
Other font styles liked:
- Calibri, cost or robotic condensed
Requirements
Must have
- sleek slim modern elegant design, ideally a white side with a frame or with our bird
Nice to have
- project progress on our website, female modern, elegant design, not too overloaded, possibility to complement our text
Should not have
- no petrol color block as on our website or as in our proposal, prefer a white background with our photo as a log,

```html
<!DOCTYPE html>
<html lang="en">
<head>
<meta charset="utf-8">
<title>Silverpine Executive Search – Executive Summary</title>
<link rel="stylesheet" href="https://fonts.googleapis.com/css2?family=Mulish:ital,wght@0,300;0,400;0,700;0,800;0,900;1,300&family=Allura&display=swap">
<style>
:root{
  --frame:#2b2b2b;
  --paper:#f6f7f8;
  --ink:#111417;
  --teal:#1b6a80;
  --band:#15657a;
  --pale:#c9dde3;
  --quote:#e8eff1;
  --line-red:#e0504a;
}
*{box-sizing:border-box;margin:0;padding:0}
html,body{width:848px;height:1200px;overflow:hidden;background:var(--frame)}
body{font-family:"Mulish",Arial,sans-serif;color:var(--ink);position:relative}
.page{position:absolute;left:24.5px;top:35px;width:799px;height:1130px;background:var(--paper);overflow:hidden}
.hero{position:absolute;left:0;top:0;width:799px;height:462px;
  background:radial-gradient(ellipse at 30% 50%,#3a3533 0%,rgba(30,28,28,0) 45%),
             radial-gradient(ellipse at 72% 45%,#4a4440 0%,rgba(30,28,28,0) 45%),
             linear-gradient(180deg,#232526 0%,#151616 60%,#0b0b0b 100%)}
.brand{position:absolute;left:37px;top:46px;display:flex;align-items:center;gap:12px}
.brand-dot{width:30px;height:30px;border-radius:50%;background:var(--pale)}
.brand-name{font-weight:300;font-size:23px;letter-spacing:3px;color:var(--pale)}
.quote{position:absolute;left:200px;top:335px;width:400px;text-align:center;font-family:"Allura",cursive;font-size:37px;line-height:41px;color:var(--quote)}
.founder{position:absolute;font-weight:300;font-size:16px;line-height:20px;color:var(--pale);letter-spacing:.2px}
.founder-left{left:37px;top:412px}
.founder-right{right:42px;top:391px;text-align:right}
.section{position:absolute}
h2{font-weight:800;font-size:15.5px;color:var(--teal);letter-spacing:-.2px;line-height:20px}
.intro{font-style:italic;font-weight:300;font-size:15.5px;line-height:20.5px;margin-top:3px}
.lead{font-weight:800;font-size:11.5px;line-height:17.5px;margin-top:6px}
p.body{font-size:12.5px;line-height:17.5px;margin-top:3px}
ul{list-style:none}
ul li{position:relative;font-size:12.5px;line-height:17.5px}
ul li::before{content:"";position:absolute;width:4px;height:4px;border-radius:50%;background:var(--ink);top:7px}
.industries{margin-top:16px}
.industries li{padding-left:16px;margin-left:13px}
.industries li::before{left:0}
.points{margin-top:5px}
.points li{padding-left:31px}
.points li::before{left:14px}
.process{position:absolute;left:24px;top:875px;width:355px;height:157px}
.locations{position:absolute;left:37px;top:1042px;font-size:15px;letter-spacing:-.2px}
.locations b{font-weight:800}
.footer{position:absolute;left:0;top:1083px;width:548px;height:47px;background:var(--band);clip-path:polygon(0 0,96% 0,100% 50%,96% 100%,0 100%)}
.contact{position:absolute;left:37px;top:12px;color:#fff;font-size:16px;letter-spacing:.1px;white-space:nowrap}
.contact span{margin:0 9px}
.social{position:absolute;top:1086px;width:30px;height:30px;border-radius:3px;background:var(--teal)}
</style>
</head>
<body>
<main class="page">
  <div class="hero" role="img" aria-label="Portrait photograph of the two founders in dark tops in front of a dim staircase"></div>
  <div class="brand"><span class="brand-dot"></span><span class="brand-name">SILVERPINE</span></div>
  <p class="quote">So they don't wear ties<br>in the boardroom anymore.<br>We never did...</p>
  <p class="founder founder-left">CLARA HOLZNER</p>
  <p class="founder founder-right">DR. MAREN LINDQVIST<br>VOGEL</p>

  <section class="section" style="left:37px;top:492px;width:340px">
    <h2>Who We are:</h2>
    <p class="intro">Founded in March 2021, by Maren &amp; Clara,<br>two years later the company has 15<br>employees</p>
  </section>

  <section class="section" style="left:37px;top:598px;width:340px">
    <h2>What we do:</h2>
    <p class="lead">While we consider ourselves a boutique Executive<br>Search Firm our span across Europe and covers multiple<br>industries:</p>
    <ul class="industries">
      <li>General Healthcare</li>
      <li>Hospitals &amp; Medical Practices</li>
      <li>Medical Technology</li>
      <li>Medical Association</li>
      <li>Education</li>
      <li>Venture Capital</li>
      <li>Private Equity</li>
      <li>Consumer</li>
    </ul>
  </section>

  <section class="section" style="left:37px;top:843px">
    <h2>Recruiting Process</h2>
  </section>

  <svg class="process" viewBox="95 1740 680 300" font-family="Mulish, Arial, sans-serif" role="img" aria-label="Recruiting process timeline from week 1 to week 12">
    <g font-size="12.5" text-anchor="middle" fill="#111">
      <text x="220" y="1760" font-weight="800">Phase 1</text>
      <text x="220" y="1779">Research - LONGLIST</text>
      <text x="434" y="1760" font-weight="800">Phase 2</text>
      <text x="434" y="1779">Focus &amp; Interviews - SHORTLIST</text>
      <text x="670" y="1760" font-weight="800">Phase 3</text>
      <text x="670" y="1779">Abschluss</text>
    </g>
    <text x="145" y="1798" font-size="10.5" font-weight="900">KW 1</text>
    <text x="755" y="1798" font-size="10.5" font-weight="900" text-anchor="end">KW 12</text>
    <line x1="145" y1="1805" x2="755" y2="1805" stroke="var(--line-red)" stroke-width="2.5"/>
    <g stroke-width="1.5">
      <line x1="181" y1="1805" x2="181" y2="1855" stroke="#7c9ba3"/>
      <line x1="290" y1="1805" x2="290" y2="1955" stroke="#6e8084"/>
      <line x1="410" y1="1805" x2="410" y2="1855" stroke="#64c0a0"/>
      <line x1="566" y1="1805" x2="566" y2="1955" stroke="#4bbfc6"/>
      <line x1="671" y1="1805" x2="671" y2="1855" stroke="#1d8fc4"/>
    </g>
    <circle cx="181" cy="1805" r="6.5" fill="#7c9ba3"/>
    <circle cx="290" cy="1805" r="6.5" fill="#6e8084"/>
    <circle cx="410" cy="1805" r="6.5" fill="#64c0a0"/>
    <circle cx="566" cy="1805" r="6.5" fill="#4bbfc6"/>
    <circle cx="671" cy="1805" r="6.5" fill="#1d8fc4"/>
    <rect x="145" y="1855" width="71" height="29" fill="#7c9ba3"/>
    <rect x="375" y="1855" width="71" height="29" fill="#64c0a0"/>
    <rect x="608" y="1855" width="129" height="29" fill="#1d8fc4"/>
    <rect x="246" y="1955" width="87" height="29" fill="#6e8084"/>
    <rect x="523" y="1955" width="87" height="29" fill="#4bbfc6"/>
    <g font-size="11.5" font-weight="800" fill="#fff" text-anchor="middle">
      <text x="180" y="1874">Kickoff</text>
      <text x="410" y="1874">Interviews</text>
      <text x="672" y="1874">Kandidatenauswahl</text>
      <text x="289" y="1974">Research</text>
      <text x="566" y="1974">Referenzen</text>
    </g>
    <g font-size="11" fill="#333" text-anchor="middle">
      <text x="180" y="1905">Abstimmung Profile,</text>
      <text x="180" y="1920">Positionsbeschreibung und</text>
      <text x="180" y="1935">Zielfirmenliste</text>
      <text x="410" y="1905">Präsentation der priorisierten</text>
      <text x="410" y="1920">Profile, Klienteninterviews</text>
      <text x="672" y="1906">Vertragsverhandlung und</text>
      <text x="672" y="1921">Onboarding, Feedback-</text>
      <text x="672" y="1936">Gespräch</text>
      <text x="289" y="2005">Aktiver und Passive Research,</text>
      <text x="289" y="2020">Ansprache pot. kandidat*innen</text>
      <text x="566" y="2005">Ggf. Assesments, Einholen von</text>
      <text x="566" y="2020">Referenzen</text>
    </g>
  </svg>

  <p class="locations"><b>Locations :</b> HAMBURG • WIEN • MÜNCHEN • DÜSSELDORF</p>

  <section class="section" style="left:438px;top:492px;width:340px">
    <h2>Leadership Advisory</h2>
    <p class="body">Our Leadership advisory services are for Management Teams as well as HR-Professionals and candidates. They are designed to help you, and your organization, to build strong and effective leadership skills and teams that can drive growth, innovation, and success.</p>
  </section>

  <section class="section" style="left:438px;top:631px;width:350px">
    <h2>How we work:</h2>
    <ul class="points">
      <li>Longstanding experience with a passion for placing C-Level Executives</li>
      <li>We work with you personally and act as an ambassador for our clients in the market</li>
      <li>Engaging in at eye-level discussion beyond just placement and HR topics</li>
      <li>Structured, lean and, most importantly, transparent digital processes, with the opportunity of 24/7 self-update on search status in our online tool</li>
      <li>Creative search approaches and comprehensive candidate evaluation</li>
      <li>Through referencing of candidates as part of the process; psychometrics on demand</li>
    </ul>
  </section>

  <section class="section" style="left:438px;top:927px;width:350px">
    <h2>By the numbers:</h2>
    <ul class="points">
      <li>95% retention rate over the course of two years</li>
      <li>30 placements made with Silverpine</li>
      <li>In total 20 years of experience in the Executive search sector</li>
      <li>Our search process – Graphik rein</li>
    </ul>
  </section>

  <footer class="footer">
    <p class="contact">www.silverpinexs.io<span>|</span>office@silverpinexs.io<span>|</span>04021/55807</p>
  </footer>
  <span class="social" style="left:595px"></span>
  <span class="social" style="left:640px"></span>
  <span class="social" style="left:684px"></span>
  <span class="social" style="left:733px"></span>
</main>
</body>
</html>
```